Business Card Design

Marla Quibbet
Artist of Contemporary/Modern/Representational Art
Contact: 0457219308
Please include my web site (thanks)! http://www.artvault913.com.au/marla-quibbet
And
Email: marlaquibbet@fernpost.example

Target Market(s)

Modern professional People who know what they like in modern contemporary art and have the means to purchase it.

Industry/Entity Type

Business

Contact Information for Business Card

Marla Quibbet
Contact: 0457219308

Font styles to use
Sans Serif

Requirements
Must have
• Simplicity & to the point
Keep the font modern/ contemporary
Nice to have
• A portrait of me and one piece of work on the business card (one on each side).
Should not have
• I'm not into butterflies.
No feminine style swirls
Nor I like swirls that look like tatoos

```html
<!DOCTYPE html>
<html lang="en">
<head>
<meta charset="utf-8">
<title>Marla Quibbet – Business Card</title>
<link rel="stylesheet" href="https://fonts.googleapis.com/css2?family=Josefin+Sans:wght@300;400&display=swap">
<style>
  :root {
    --page: #ffffff;
    --card: #050505;
    --accent: #d2505a;
    --ink: #f4f4f4;
    --frame: #f1efe8;
    --portrait-a: #6b5447;
    --portrait-b: #c46a3a;
    --art-one-a: #c9a23a;
    --art-one-b: #b4394a;
    --art-two-a: #b85a3a;
    --art-two-b: #7a8a9a;
    --shadow: rgba(0, 0, 0, 0.25);
  }

  * { box-sizing: border-box; margin: 0; padding: 0; }

  html, body {
    width: 1200px;
    height: 900px;
    overflow: hidden;
    background: var(--page);
  }

  .canvas {
    position: relative;
    width: 1200px;
    height: 900px;
  }

  .card {
    position: absolute;
    left: 320px;
    width: 560px;
    height: 310px;
    background: var(--card);
    box-shadow: 0 3px 10px var(--shadow);
    overflow: hidden;
    font-family: "Josefin Sans", sans-serif;
  }

  .card--front { top: 120px; }
  .card--back  { top: 470px; }

  .card__name {
    font-family: "Josefin Sans", sans-serif;
    font-variant: small-caps;
    color: var(--accent);
    letter-spacing: 0.18em;
    font-weight: 400;
  }

  /* Front */
  .card--front .card__name {
    position: absolute;
    left: 30px;
    top: 26px;
    font-size: 30px;
  }

  .portrait {
    position: absolute;
    left: 108px;
    top: 88px;
    width: 112px;
    height: 170px;
    border: 5px solid var(--frame);
    background: radial-gradient(circle at 50% 40%, var(--portrait-b), var(--portrait-a) 75%);
  }

  .artwork {
    position: absolute;
    left: 318px;
    width: 232px;
    height: 138px;
    border: 5px solid var(--frame);
  }

  .artwork--houses {
    top: 10px;
    background: linear-gradient(135deg, var(--art-one-a), var(--art-one-b));
  }

  .artwork--town {
    top: 158px;
    background: linear-gradient(160deg, var(--art-two-b), var(--art-two-a) 55%);
  }

  /* Back */
  .card--back {
    text-align: center;
    color: var(--ink);
    font-weight: 300;
  }

  .card--back .card__name {
    margin-top: 34px;
    font-size: 30px;
  }

  .card__rule {
    width: 270px;
    height: 1px;
    margin: 12px auto 0;
    background: var(--ink);
    border: 0;
  }

  .card__role {
    margin-top: 28px;
    font-size: 16px;
  }

  .card__web {
    margin-top: 12px;
    font-size: 18px;
    font-weight: 400;
  }

  .card__email {
    margin-top: 10px;
    font-size: 15px;
  }

  .card__phone {
    margin-top: 20px;
    font-size: 14px;
    letter-spacing: 0.04em;
  }
</style>
</head>
<body>
  <main class="canvas">
    <section class="card card--front" aria-label="Business card front">
      <h1 class="card__name">Marla Quibbet</h1>
      <div class="portrait" role="img" aria-label="Portrait photograph of the artist"></div>
      <div class="artwork artwork--houses" role="img" aria-label="Painting of colourful houses and trees"></div>
      <div class="artwork artwork--town" role="img" aria-label="Painting of a red-roofed town seen from above"></div>
    </section>

    <section class="card card--back" aria-label="Business card back">
      <h2 class="card__name">Marla Quibbet</h2>
      <hr class="card__rule">
      <p class="card__role">Artist of Contemporary/Modern/Representational art</p>
      <p class="card__web">www.artvault913.com.au/marla-quibbet</p>
      <p class="card__email">marlaquibbet@fernpost.example</p>
      <p class="card__phone">0457219308</p>
    </section>
  </main>
</body>
</html>
```